Velmora Limited Business Card Design Project

Velmora Limited is my UK based company used as my brand to work as an Interim Manager or contractor in project/programme management and Non-Executive Director.

Velmora is Latin for 'execute' as in getting things done rather than killing people!

Logo and design needs to promote reliable, professional, and successful project delivery. Simple, elegant, clean, professional are words that should spring to mind!
Updates

Target Market(s)

Middle and senior management in english speaking countries aged 35 - 60 that hire and task qualified and experienced project/programme managers and Non-Executive Directors.

Industry/Entity Type

Contractor

Font styles to use
Serif
Sans Serif

Requirements
Must have
• Mobile telephone number 07840 512697
email address peterhalloway@velmora.co.uk
Nice to have
• LinkedIn link to my profile.

Interim Manager
Should not have
• avoid Ticks and clocks

```html
<!DOCTYPE html>
<html lang="en">
<head>
<meta charset="utf-8">
<title>Velmora Limited – Business Card</title>
<link rel="stylesheet" href="https://fonts.googleapis.com/css2?family=Cormorant+Garamond:wght@600&family=Questrial&display=swap">
<style>
  :root {
    --navy: #0b3a82;
    --navy-deep: #062c68;
    --paper: #ffffff;
    --ink: #4a4a4a;
    --rule: #b9b9b9;
    --backdrop: #e9eaec;
  }
  * { box-sizing: border-box; margin: 0; padding: 0; }
  html, body { width: 1200px; height: 900px; overflow: hidden; }
  body {
    background: var(--backdrop);
    position: relative;
    font-family: "Questrial", "Century Gothic", sans-serif;
  }
  .card {
    position: absolute;
    width: 700px;
    height: 400px;
    box-shadow: 0 10px 30px rgba(0,0,0,.18);
  }
  .card-front { left: 420px; top: 50px; background: var(--paper); }
  .card-back {
    left: 80px; top: 470px;
    background: linear-gradient(135deg, var(--navy) 0%, var(--navy-deep) 100%);
    display: flex; align-items: center; justify-content: center;
  }
  .wordmark {
    font-family: "Cormorant Garamond", "Times New Roman", serif;
    font-weight: 600;
    text-transform: uppercase;
    text-align: center;
    white-space: nowrap;
    line-height: 1.05;
  }
  .wordmark-line { display: block; }
  .card-front .wordmark {
    position: absolute; left: 30px; width: 340px; top: 130px;
    font-size: 46px; letter-spacing: 4px;
    color: var(--navy);
  }
  .card-back .wordmark {
    font-size: 64px; letter-spacing: 6px;
    color: var(--paper);
  }
  .divider {
    position: absolute; left: 395px; top: 70px;
    width: 1px; height: 260px; background: var(--rule);
  }
  .contact { position: absolute; left: 420px; top: 78px; }
  .person-name { color: var(--navy); font-size: 26px; line-height: 1.1; }
  .person-role { color: var(--ink); font-size: 17px; margin-bottom: 22px; }
  .contact-list { list-style: none; }
  .contact-item {
    display: flex; align-items: center; gap: 12px;
    color: var(--ink); font-size: 15px; margin-bottom: 12px;
  }
  .icon-box {
    width: 26px; height: 26px; background: var(--navy);
    display: flex; align-items: center; justify-content: center;
    border-radius: 2px; flex: none;
  }
  .icon-box svg { width: 18px; height: 18px; }
</style>
</head>
<body>
  <section class="card card-front" aria-label="Card front">
    <div class="wordmark">
      <span class="wordmark-line">Velmora</span>
      <span class="wordmark-line">Limited</span>
    </div>
    <div class="divider"></div>
    <div class="contact">
      <div class="person-name">Peter Halloway</div>
      <div class="person-role">Interim Manager</div>
      <ul class="contact-list">
        <li class="contact-item">
          <span class="icon-box"><svg viewBox="0 0 18 18"><rect x="5" y="2" width="8" height="14" rx="1.5" fill="none" stroke="#fff" stroke-width="1.4"/><rect x="6.8" y="4" width="4.4" height="5" fill="#fff"/><circle cx="9" cy="13" r="1" fill="#fff"/></svg></span>
          07840 512697
        </li>
        <li class="contact-item">
          <span class="icon-box"><svg viewBox="0 0 18 18" fill="none" stroke="#fff" stroke-width="1.2"><circle cx="9" cy="9" r="6.5"/><ellipse cx="9" cy="9" rx="3" ry="6.5"/><line x1="2.5" y1="9" x2="15.5" y2="9"/><line x1="3.5" y1="5.5" x2="14.5" y2="5.5"/><line x1="3.5" y1="12.5" x2="14.5" y2="12.5"/></svg></span>
          www.velmora.co.uk
        </li>
        <li class="contact-item">
          <span class="icon-box"><svg viewBox="0 0 18 18" fill="none" stroke="#fff" stroke-width="1.3"><rect x="2.5" y="4.5" width="13" height="9"/><polyline points="2.5,4.5 9,10 15.5,4.5"/></svg></span>
          peterhalloway@velmora.co.uk
        </li>
        <li class="contact-item">
          <span class="icon-box"><svg viewBox="0 0 18 18" fill="none" stroke="#fff" stroke-width="1.5"><rect x="1.8" y="6.2" width="8" height="5.6" rx="2.8"/><rect x="8.2" y="6.2" width="8" height="5.6" rx="2.8"/></svg></span>
          linkprofile.net/user
        </li>
      </ul>
    </div>
  </section>

  <section class="card card-back" aria-label="Card back">
    <div class="wordmark">
      <span class="wordmark-line">Velmora</span>
      <span class="wordmark-line">Limited</span>
    </div>
  </section>
</body>
</html>
```